Travel Poster Design Project

A poster design for a specific Adventure Travel Journey to Ladakh India. The journey it will be promoting is a 2 week trekking and cultural tour through Ladakh passing over 2 mountain passes in excess of 5000 meters.

Dates are July and August each year

Brand Name is Farwind Treks

We do inspiring unique journeys in a small select number of locations around the world. Ladakh is also known as Little Tibet and has a buddhist culture

We have a logo already to use and we also have a range of photos online for you to select from. They can be seen at http://images.brookpaddle.example/FarwindTreks then click on Ladakh

Target Market(s)

Adventure travel people 30-55 poster will be displayed in our rafting retail base so will be seen by target market

Industry/Entity Type

Travel

Requirements
Must have
• website address www.farwindtreks.example
Phone Number 01632 960418
email info@farwindtreks.example
Pictures
small legal note along the bottom, saying Farwind Treks is a brand name of Torrent Ridge River Sports LLP
Nice to have
• Lots of inspiring photos and colour
Should not have
• named dates

```html
<!DOCTYPE html>
<html lang="en">
<head>
<meta charset="utf-8">
<title>Farwind Treks – Adventure Travel Journey to Ladakh India</title>
<link href="https://fonts.googleapis.com/css2?family=Arimo:wght@400;700&display=swap" rel="stylesheet">
<style>
  :root{
    --orange:#f39a1e;
    --orange-light:#f7b347;
    --white:#ffffff;
    --ink:#2a2a2a;
    --brand-blue:#1c5fa8;
    --gap:#ffffff;
  }
  *{margin:0;padding:0;box-sizing:border-box}
  html,body{width:849px;height:1200px;overflow:hidden;background:#fff}
  .poster{position:relative;width:849px;height:1200px;overflow:hidden;background:var(--gap);font-family:'Arimo',Arial,sans-serif}
  .photo{position:absolute}
  .photo--peaks{left:0;top:0;width:280px;height:170px;background:linear-gradient(180deg,#4f86c2 0%,#9fb9d6 45%,#6c6a66 75%,#4d4a46 100%)}
  .photo--palace{left:284px;top:0;width:266px;height:172px;background:linear-gradient(180deg,#6fa3d8 0%,#c9dbee 40%,#d8d0bd 70%,#8f8472 100%)}
  .photo--flags{left:554px;top:0;width:295px;height:408px;background:linear-gradient(135deg,#c8d8ea 0%,#d9c36a 30%,#c43a2f 50%,#3c77c2 70%,#e7e2d2 100%)}
  .photo--stupa{left:0;top:174px;width:550px;height:802px;background:linear-gradient(180deg,#3f7bd0 0%,#7eaee3 30%,#e9edf2 55%,#c9c3b5 75%,#9c7f55 100%)}
  .photo--monastery{left:554px;top:412px;width:295px;height:166px;background:linear-gradient(180deg,#6f9fd6 0%,#b7cbe0 40%,#b9a789 70%,#8a7459 100%)}
  .photo--buddha{left:554px;top:582px;width:295px;height:394px;background:linear-gradient(160deg,#2f3f7a 0%,#5a5f9c 30%,#d7a64a 60%,#a66a2c 100%)}
  .headline-word{position:absolute;left:40px;color:var(--white);opacity:.82;font-weight:700;line-height:1;white-space:nowrap}
  .headline-word--travel{top:318px;font-size:168px;letter-spacing:-8px}
  .headline-word--to{top:530px;font-size:86px;letter-spacing:-4px}
  .headline-word--discover{top:730px;font-size:140px;letter-spacing:-9px}
  .panel{position:absolute;left:0;top:976px;width:849px;height:224px;background:linear-gradient(90deg,var(--orange) 0%,var(--orange-light) 100%)}
  .panel__title{position:absolute;left:78px;top:30px;color:var(--white);font-weight:700;font-size:29px;line-height:1.12}
  .panel__text{position:absolute;left:78px;top:106px;width:420px;color:var(--white);font-size:11.5px;font-weight:700;line-height:1.35}
  .contact{position:absolute;left:60px;top:140px;width:292px;height:84px;background:var(--white);padding:18px 18px;color:var(--orange);font-size:12px;line-height:1.45;font-weight:700}
  .contact span{display:block}
  .brand-name{position:absolute;left:368px;top:152px;color:var(--ink);font-weight:700;font-size:26px;white-space:nowrap}
  .brand-badge{position:absolute;left:628px;top:8px;width:180px;height:180px;border-radius:50%;background:var(--brand-blue);display:flex;align-items:center;justify-content:center;color:var(--white);font-weight:700;font-size:24px;text-align:center;line-height:1.15}
  .legal{position:absolute;left:598px;top:198px;width:240px;color:var(--ink);font-size:7.5px;text-align:center;line-height:1.3}
</style>
</head>
<body>
<main class="poster">
  <div class="photo photo--peaks" role="img" aria-label="Snow-capped Himalayan peaks under a blue sky"></div>
  <div class="photo photo--palace" role="img" aria-label="White Ladakhi palace with domed tower against blue sky"></div>
  <div class="photo photo--flags" role="img" aria-label="Colourful Buddhist prayer flags fluttering in the wind"></div>
  <div class="photo photo--stupa" role="img" aria-label="Large white Buddhist stupa beneath a deep blue sky with mountains behind"></div>
  <div class="photo photo--monastery" role="img" aria-label="Hillside monastery buildings in Ladakh"></div>
  <div class="photo photo--buddha" role="img" aria-label="Golden Buddha statue inside a monastery"></div>

  <h1 class="headline">
    <span class="headline-word headline-word--travel">TRAVEL</span>
    <span class="headline-word headline-word--to">TO</span>
    <span class="headline-word headline-word--discover">DISCOVER</span>
  </h1>

  <section class="panel">
    <h2 class="panel__title">Adventure Travel Journey<br>to Ladakh India.</h2>
    <p class="panel__text">Enjoy a 2 week trekking and cultural tour through Ladakh passing over 2 mountain passes in excess of 5000 meters in July and August each year.</p>
    <div class="contact">
      <span>www.farwindtreks.example</span>
      <span>Phone: 01632 960418</span>
      <span>E-mail: info@farwindtreks.example</span>
    </div>
    <div class="brand-name">Farwind Treks</div>
    <div class="brand-badge">Farwind<br>Treks</div>
    <p class="legal">Farwind Treks is a brand name of Torrent Ridge River Sports LLP</p>
  </section>
</main>
</body>
</html>
```